BLORK Business Card

Quellmont Dwelling Additions and Refits. I need a business card designed for this new high end renovation business. I would like the logo centered on the back side with the ABN (71 903 226 417) on the bottom right hand corner.

I would like the following information placed on the other side along with some customized pattern or design.

Percival Oakden
Director
Phone: 1300 418 957
Fax: (02) 9316 4471
Website: www.blorkbuilding.com.au
Email: p.oakden@blorkbuilding.com.au
PO Box 87,
Wendlecove NSW 2094

(FB Logo) BLORK - Quellmont Dwelling Additions and Refits

The final design should communicate professionalism and trust.

Back side background colour: white
Front side: Undecided

```html
<!DOCTYPE html>
<html lang="en">
<head>
<meta charset="utf-8">
<title>BLORK Business Card</title>
<link rel="stylesheet" href="https://fonts.googleapis.com/css2?family=Cinzel:wght@400;600&family=Montserrat:wght@400;500&display=swap">
<style>
  :root {
    --page: #e9ebec;
    --teal-light: #169fb2;
    --teal-dark: #0d5d6d;
    --gold: #f3e08a;
    --white: #ffffff;
    --navy: #1f3a8a;
    --ink: #1b1f24;
    --grey: #8a8a8a;
    --rule: rgba(255,255,255,0.75);
    --faint: rgba(255,255,255,0.12);
  }
  * { box-sizing: border-box; margin: 0; padding: 0; }
  html, body { width: 1200px; height: 1029px; overflow: hidden; }
  body { background: var(--page); position: relative; font-family: "Montserrat", sans-serif; }

  .card {
    position: absolute; left: 220px; width: 760px; height: 463px;
    box-shadow: 0 6px 18px rgba(0,0,0,0.18);
    overflow: hidden;
  }

  /* Front: contact side */
  .card-front { top: 36px; background: var(--teal-dark); }
  .front-panel-left {
    position: absolute; left: 0; top: 0; width: 300px; height: 100%;
    background: var(--teal-light);
  }
  .front-watermark {
    position: absolute; left: 38px; top: 250px;
    color: var(--faint); font-family: "Montserrat", sans-serif;
    font-size: 64px; font-weight: 500; line-height: 1; letter-spacing: 2px;
  }

  .identity { position: absolute; left: 38px; top: 96px; }
  .identity .name {
    font-family: "Cinzel", serif; font-weight: 600; color: var(--gold);
    font-size: 28px; letter-spacing: 1px; white-space: nowrap;
  }
  .identity .role {
    font-family: "Cinzel", serif; color: var(--gold);
    font-size: 17px; letter-spacing: 22px; margin-top: 10px; padding-left: 4px;
  }
  .front-rule { position: absolute; left: 130px; top: 186px; width: 490px; height: 1px; background: var(--rule); }

  .contact-list {
    position: absolute; left: 330px; top: 206px; list-style: none;
    color: var(--white); font-size: 14px; letter-spacing: 1px; text-transform: uppercase;
  }
  .contact-list li { display: flex; margin-bottom: 14px; }
  .contact-list .label { width: 34px; }

  .social-band {
    position: absolute; left: 0; bottom: 0; width: 100%; height: 70px;
    background: rgba(0,0,0,0.14); display: flex; align-items: center; padding-left: 30px;
    color: var(--white); font-size: 14px; letter-spacing: 5px; text-transform: uppercase;
  }
  .social-band .dot { width: 22px; height: 22px; background: var(--white); opacity: 0.85; margin-right: 16px; }

  /* Back: logo side */
  .card-back { top: 530px; background: var(--white); }
  .back-frame-top {
    position: absolute; left: 24px; top: 24px; width: 690px; height: 395px;
    border-top: 5px solid var(--navy); border-left: 5px solid var(--navy);
  }
  .back-frame-bottom {
    position: absolute; left: 46px; top: 44px; width: 690px; height: 395px;
    border-right: 5px solid var(--ink); border-bottom: 5px solid var(--ink);
  }
  .brand {
    position: absolute; left: 0; top: 165px; width: 100%; text-align: center;
  }
  .brand .brand-name {
    font-family: "Montserrat", sans-serif; font-weight: 500; color: var(--navy);
    font-size: 64px; line-height: 1; letter-spacing: 4px;
  }
  .brand .brand-web {
    font-family: "Montserrat", sans-serif; color: var(--ink);
    font-size: 13px; letter-spacing: 7px; margin-top: 26px;
  }
  .abn {
    position: absolute; right: 60px; bottom: 70px;
    font-family: "Cinzel", serif; color: var(--grey); font-size: 14px;
  }
</style>
</head>
<body>

<section class="card card-front">
  <div class="front-panel-left"></div>
  <div class="front-watermark" aria-hidden="true">BLORK</div>
  <div class="identity">
    <div class="name">Percival Oakden</div>
    <div class="role">DIRECTOR</div>
  </div>
  <div class="front-rule"></div>
  <ul class="contact-list">
    <li><span class="label">P:</span><span>1300 418 957</span></li>
    <li><span class="label">F:</span><span>(02) 9316 4471</span></li>
    <li><span class="label">A:</span><span>PO Box 87, Wendlecove NSW 2094</span></li>
    <li><span class="label">W:</span><span>www.blorkbuilding.com.au</span></li>
    <li><span class="label">E:</span><span>p.oakden@blorkbuilding.com.au</span></li>
  </ul>
  <div class="social-band">
    <span class="dot"></span>
    <span>https://www.chatterlane.com/quellmontrefits1</span>
  </div>
</section>

<section class="card card-back">
  <div class="back-frame-top"></div>
  <div class="back-frame-bottom"></div>
  <div class="brand">
    <div class="brand-name">BLORK</div>
    <div class="brand-web">www.blorkbuilding.com.au</div>
  </div>
  <div class="abn">ABN: 71 903 226 417</div>
</section>

</body>
</html>
```